AI Discovery Workshop Presentation

We have a wireframe presentation with 43 slides (many with the same format) to be implemented in Powerpoint. We provide Corporate presentation in order to reuse template. Please, be creative and don't take the examples in the wireframe as literal. We also provide the following:
- Color palette
- bytefolk Logos
- Slide wireframe
- Flyer
- bytefolk Corporate Presentation. Please, use this as a general template.
You can find all the materials here:
https://files.vantorbox.net/share/7QmZp2LxR9dKw4TnB8yHc3VfJ5sEaU0?usp=sharing

```html
<!DOCTYPE html>
<html lang="en">
<head>
<meta charset="utf-8">
<title>AI Discovery Workshop – Slide Overview</title>
<link rel="stylesheet" href="https://fonts.googleapis.com/css2?family=Noto+Sans:wght@400;600;700;800&family=Poppins:wght@400;600&display=swap">
<style>
:root{
  --page:#f4f6fb;
  --navy:#0c2a44;
  --ink:#0a1a2e;
  --teal:#1fa195;
  --teal-soft:#2b6f78;
  --purple:#8b0b82;
  --white:#ffffff;
}
*{box-sizing:border-box;margin:0;padding:0}
html,body{width:1200px;height:1032px;overflow:hidden;background:var(--page)}
body{position:relative;font-family:"Noto Sans",sans-serif;color:var(--navy)}
.slide{position:absolute;width:461px;height:259px;background:var(--white);overflow:hidden;box-shadow:0 6px 18px rgba(20,30,60,.18)}
.col-left{left:127px}.col-right{left:612px}
.row-1{top:104px}.row-2{top:387px}.row-3{top:670px}
.abs{position:absolute}
.slide-title{position:absolute;left:20px;top:13px;font-size:17px;font-weight:700;color:var(--navy);white-space:nowrap}
.slide-title .accent{color:var(--teal)}
.footer-band{position:absolute;left:0;right:0;top:235px;height:15px;
  background:linear-gradient(90deg,#0c1d38 0%,#0f3b52 25%,#1b6f76 45%,#123552 70%,#3a2360 100%);}
.footer-logo{position:absolute;left:17px;top:2px;font-size:8px;font-weight:700;color:var(--white);display:flex;align-items:center;gap:2px}
.footer-logo .mark{width:4px;height:4px;background:var(--teal)}
.page-num{position:absolute;right:16px;top:3px;font-size:6.5px;color:var(--white)}

/* Cover */
.cover{background:
  radial-gradient(ellipse 260px 70px at 180px 0,rgba(40,150,150,.75),transparent 70%),
  radial-gradient(ellipse 150px 60px at 440px 0,rgba(150,60,150,.75),transparent 70%),
  linear-gradient(180deg,#12294a 0%,#0b1a2f 45%,#08172a 100%);}
.cover-logo{left:36px;top:52px;font-size:21px;font-weight:700;color:var(--white);display:flex;align-items:center;gap:4px}
.cover-logo .mark{width:10px;height:10px;background:var(--teal)}
.cover-title{left:36px;top:112px;font-size:32px;font-weight:800;color:var(--white)}
.cover-sub{left:36px;top:150px;font-size:19px;font-weight:700;color:var(--teal)}
.cover-link{left:36px;top:185px;width:84px;height:17px;border:1px solid var(--white);border-radius:3px;font-size:8.5px;font-weight:600;color:var(--teal);display:flex;align-items:center;justify-content:center}
.cover-bar{position:absolute;background:var(--teal-soft);opacity:.8}
.cover-visual{left:229px;top:131px;width:202px;height:202px;border-radius:50%;
  background:radial-gradient(circle at 52% 48%,#4fc6f0 0%,#1d5a9a 18%,#10305a 45%,#0a1a30 80%)}

/* Introductions */
.portrait-frame{left:75px;top:61px;width:137px;height:137px;border:1.5px solid var(--teal);border-radius:6px;padding:5px}
.portrait{width:100%;height:100%;border-radius:4px;background:linear-gradient(160deg,#d9d6d0 0%,#9fb4ae 45%,#2e8c84 100%)}
.profile{left:232px;top:68px;width:200px}
.profile dt{font-size:8.5px;font-weight:700;color:var(--ink);line-height:11px}
.profile dd{font-size:11.5px;font-weight:700;color:var(--teal);line-height:14px;margin-bottom:4px}
.profile dd.note{font-size:7px;font-weight:400;line-height:8.6px}

/* About us */
.about-panel{left:0;top:54px;width:461px;height:156px;background:
  radial-gradient(ellipse 200px 40px at 180px 0,rgba(40,150,150,.6),transparent 70%),
  radial-gradient(ellipse 140px 40px at 450px 0,rgba(150,60,150,.6),transparent 70%),
  linear-gradient(180deg,#122c4b 0%,#0a1a30 60%,#08162a 100%);}
.about-heading{left:0;width:461px;top:72px;text-align:center;font-family:"Poppins",sans-serif;font-weight:600;font-size:21.5px;line-height:29px;color:var(--teal)}
.about-body{left:49px;top:149px;width:370px;font-family:"Poppins",sans-serif;font-size:11.2px;line-height:15.6px;color:var(--white)}

/* Workshop */
.objective{left:81px;top:48px;width:320px;font-size:11.8px;line-height:14px;color:var(--ink)}
.objective strong{color:var(--teal)}
.pillar-label{position:absolute;width:110px;text-align:center;font-size:11px;font-weight:700;line-height:13.5px;color:var(--teal)}

/* Agenda */
.stage-label{font-size:11.8px;font-weight:700;fill:var(--white);font-family:"Noto Sans",sans-serif}

/* AI */
.ai-visual{left:75px;top:70px;width:130px;height:130px;border-radius:50%;
  background:radial-gradient(circle at 50% 45%,#3a8ee0 0%,#1a4fa0 35%,#0e2c6a 70%,#0a1c48 100%)}
.ai-def{left:241px;top:92px;width:160px;font-size:11.8px;font-weight:700;line-height:13.8px;color:var(--ink)}
</style>
</head>
<body>

<!-- Cover -->
<section class="slide cover col-left row-1">
  <div class="cover-bar" style="left:268px;top:85px;width:34px;height:64px"></div>
  <div class="cover-bar" style="left:314px;top:61px;width:34px;height:88px"></div>
  <div class="cover-bar" style="left:359px;top:36px;width:34px;height:113px"></div>
  <div class="abs cover-visual" role="img" aria-label="Photo of a human hand and a robotic hand reaching toward a glowing point over a circuit board"></div>
  <div class="abs cover-logo"><span class="mark"></span>bytefolk</div>
  <h1 class="abs cover-title">AI Discovery</h1>
  <div class="abs cover-sub">Workshop</div>
  <div class="abs cover-link">Bytefolk.cloud</div>
</section>

<!-- Introductions -->
<section class="slide col-right row-1">
  <h2 class="slide-title">Introductions</h2>
  <div class="abs portrait-frame"><div class="portrait" role="img" aria-label="Portrait photo of the presenter standing in an office"></div></div>
  <dl class="abs profile">
    <dt>Name:</dt><dd>Mara Quinlan</dd>
    <dt>Department:</dt><dd>Business Development</dd>
    <dt>Role:</dt><dd>Business Analytics</dd>
    <dt>Workshop expectations:</dt>
    <dd class="note">Lorem ipsum dolor sit amet, consectetur adipiscing elit, sed do eiusmod tempor incididunt ut labore et dolore magna aliqua.</dd>
  </dl>
  <div class="footer-band"><div class="footer-logo"><span class="mark"></span>bytefolk</div><span class="page-num">1</span></div>
</section>

<!-- About us -->
<section class="slide col-left row-2">
  <h2 class="slide-title" style="top:16px">About <span class="accent">us</span></h2>
  <div class="abs about-panel"></div>
  <div class="abs about-heading">Data Analytics &amp; AI<br>for Nonconformists</div>
  <p class="abs about-body">We are a leading Professional Services company specialized in the design and implementation of cutting edge technologies in Cloud, Data Analytics &amp; AI.</p>
  <div class="footer-band"><div class="footer-logo"><span class="mark"></span>bytefolk</div><span class="page-num">2</span></div>
</section>

<!-- About the Workshop -->
<section class="slide col-right row-2">
  <h2 class="slide-title" style="top:12px">About <span class="accent">the Workshop</span></h2>
  <p class="abs objective">The objective of the workshop is&nbsp; for you to discover feasible and high-impact <strong>AI use cases</strong></p>
  <svg class="abs" style="left:0;top:0" width="461" height="235" viewBox="0 0 461 235">
    <g fill="none" stroke="#1fa195" stroke-width="1.2">
      <path d="M229 83V102M122 102H337M122 102V116M229 102V116M337 102V116"/>
    </g>
    <g fill="#0c2a44"><circle cx="122" cy="145" r="30"/><circle cx="229" cy="145" r="30"/><circle cx="337" cy="145" r="30"/></g>
    <g fill="none" stroke="#fff" stroke-width="1.8" stroke-linecap="round" stroke-linejoin="round">
      <circle cx="119" cy="137" r="6"/><path d="M108 160v-4a8 8 0 0 1 8-8h6"/><circle cx="131" cy="154" r="5"/><path d="M129 155q2 2 4 0"/>
      <rect x="214" y="130" width="11" height="8" rx="1"/><rect x="233" y="131" width="12" height="8" rx="1"/><rect x="214" y="149" width="11" height="8" rx="1"/><circle cx="238" cy="153" r="5"/><path d="M236 153l1.5 1.5 3-3"/><path d="M213 125l3 3m0-3l-3 3"/>
      <path d="M325 160v-5M330 160v-8M335 160v-11M340 160v-14M345 160v-20"/><circle cx="330" cy="144" r="5"/><path d="M330 144l10-10M345 137v-10l-3 3m3-3 3 3"/>
    </g>
  </svg>
  <div class="pillar-label" style="left:67px;top:183px">You, not us</div>
  <div class="pillar-label" style="left:174px;top:183px">Feasible, not impossible</div>
  <div class="pillar-label" style="left:282px;top:183px">High impact</div>
  <div class="footer-band"><div class="footer-logo"><span class="mark"></span>bytefolk</div><span class="page-num">3</span></div>
</section>

<!-- Agenda -->
<section class="slide col-left row-3">
  <h2 class="slide-title">Agenda</h2>
  <svg class="abs" style="left:0;top:0" width="461" height="235" viewBox="0 0 461 235">
    <circle cx="107" cy="129" r="47" fill="#1fa195" stroke="#0c2a44" stroke-width="3"/>
    <circle cx="230" cy="129" r="47" fill="#8b0b82" stroke="#1fa195" stroke-width="3"/>
    <circle cx="354" cy="129" r="47" fill="#062a44" stroke="#1fa195" stroke-width="3"/>
    <g fill="none" stroke-width="1.6" stroke-linecap="round" stroke-linejoin="round">
      <path d="M157 129H177M171 123l6 6-6 6" stroke="#0c2a44"/>
      <path d="M280 129H302M296 123l6 6-6 6" stroke="#1fa195"/>
    </g>
    <g text-anchor="middle" class="stage-label">
      <text class="stage-label" x="107" y="125">Inspire</text><text class="stage-label" x="107" y="139">(60 minutes)</text>
      <text class="stage-label" x="230" y="125">Discover</text><text class="stage-label" x="230" y="139">(60 minutes)</text>
      <text class="stage-label" x="354" y="125">Prioritize</text><text class="stage-label" x="354" y="139">(90 minutes)</text>
    </g>
  </svg>
  <div class="footer-band"><div class="footer-logo"><span class="mark"></span>bytefolk</div><span class="page-num">3</span></div>
</section>

<!-- Artificial Intelligence -->
<section class="slide col-right row-3">
  <h2 class="slide-title">Artificial <span class="accent">Intelligence</span></h2>
  <svg class="abs" style="left:0;top:0" width="461" height="235" viewBox="0 0 461 235"><circle cx="140" cy="135" r="76" fill="none" stroke="#1fa195" stroke-width="2"/></svg>
  <div class="abs ai-visual" role="img" aria-label="Illustration of a glowing AI processor chip on a blue circuit board"></div>
  <p class="abs ai-def">It is the general field of computer science dedicated to creating machines that can simulate human intelligence</p>
  <div class="footer-band"><div class="footer-logo"><span class="mark"></span>bytefolk</div><span class="page-num">3</span></div>
</section>

</body>
</html>
```